Wirenexa

I'm looking to much improve our current website wirenexa.com
Updates

Low design quality

Target Market(s)

Commercial clients (Not-Residentials)

Industry/Entity Type

Office buildings and Industrial clients

Coding

Coded - Design and coding required

Number of Pages Required

5+ page

Requirements
Must have
• Very professional structured low voltage cabling projects for Wi-Fi, Audio/Video conference rooms, Access Control systems, CCTV.

```html
<!DOCTYPE html>
<html lang="en">
<head>
<meta charset="utf-8">
<title>Wirenexa – Professional Cabling</title>
<link href="https://fonts.googleapis.com/css2?family=Inter:wght@400;500;600;700;800&display=swap" rel="stylesheet">
<style>
:root{
  --red:#d42e22;
  --black:#000;
  --ink:#111;
  --text:#444;
  --line:#e2e2e2;
  --footer:#f6eff0;
  --white:#fff;
}
*{box-sizing:border-box;margin:0;padding:0}
html,body{width:1200px;height:4110px;overflow:hidden}
body{font-family:'Inter',sans-serif;color:var(--ink);background:var(--white);position:relative}
.abs{position:absolute}
/* header */
.site-header{position:absolute;left:0;top:0;width:1200px;height:86px;background:var(--white)}
.brand{position:absolute;left:167px;top:28px;display:flex;align-items:center;gap:6px;font-weight:800;font-size:26px;color:var(--red);letter-spacing:-.5px}
.brand-mark{width:18px;height:18px;background:var(--red)}
.nav{position:absolute;left:440px;top:34px;display:flex;gap:31px;font-size:14px}
.nav .active{color:var(--red)}
.phone-btn{position:absolute;left:875px;top:26px;width:159px;height:35px;border-radius:18px;background:var(--red);color:#fff;font-size:14px;font-weight:500;display:flex;align-items:center;justify-content:center;gap:8px}
/* hero */
.hero{position:absolute;left:0;top:86px;width:1200px;height:720px;background:linear-gradient(110deg,#05080c 0%,#0d1a24 40%,#1f4d6b 70%,#163247 100%)}
.hero-title{position:absolute;left:167px;top:250px;font-size:50px;line-height:58px;font-weight:700;color:#fff}
.hero-regions{position:absolute;left:167px;top:446px;font-size:19px;color:var(--red);letter-spacing:.5px}
.callback{position:absolute;left:680px;top:97px;width:354px;height:527px;background:#fff;border-radius:24px;padding:32px 25px}
.callback h2{font-size:25px;font-weight:700;margin-bottom:14px}
.field{height:40px;border:1px solid var(--line);border-radius:6px;font-size:13px;color:#aaa;padding:12px 13px;margin-bottom:17px}
.field.msg{height:104px}
.captcha{height:77px;border:1px solid #d3d3d3;border-radius:4px;background:#f9f9f9;display:flex;align-items:center;padding:0 12px;gap:12px;font-size:13px;color:#222}
.captcha .box{width:27px;height:27px;border:2px solid #c1c1c1;border-radius:3px;background:#fff}
.btn-red{height:32px;border-radius:16px;background:var(--red);color:#fff;font-size:13px;font-weight:600;display:flex;align-items:center;justify-content:center}
/* intro */
.center{text-align:center}
.h-sec{font-size:33px;font-weight:600;line-height:42px}
.p-sec{font-size:13px;line-height:18px;color:var(--text)}
.feature-photo{position:absolute;left:167px;top:1137px;width:353px;height:428px;background:linear-gradient(90deg,#c99a1c 0%,#e6b83a 25%,#9fa7ae 55%,#d9dcdf 100%)}
.features{position:absolute;left:606px;top:1138px;width:430px}
.features h3{font-size:20px;font-weight:600;margin-bottom:20px}
.features p{font-size:12.5px;line-height:18px;color:var(--text);margin-bottom:16px}
.features p b{color:var(--ink);font-weight:600}
.ticks li{list-style:none;display:flex;align-items:center;gap:10px;font-size:13px;font-weight:500;margin-bottom:17px}
/* why */
.why-card{position:absolute;top:1808px;width:280px;height:259px;border:1px solid var(--line);border-radius:14px;text-align:center;padding:30px 24px}
.why-card.hot{background:var(--red);border-color:var(--red);color:#fff}
.why-card h4{font-size:20px;font-weight:500;margin:22px 0 10px}
.why-card p{font-size:13px;line-height:18px;color:var(--text)}
.why-card.hot p{color:#fff}
.why-card .more{display:inline-block;margin-top:14px;font-size:13px;text-decoration:underline}
/* service band */
.band{position:absolute;top:2150px;height:300px;color:#fff;text-align:center;display:flex;flex-direction:column;align-items:center;justify-content:center}
.band h4{font-size:20px;font-weight:600;margin-bottom:12px}
.band p{font-size:13px;line-height:18px;width:240px}
.band .cta{margin-top:22px;width:158px;height:32px;display:flex;align-items:center;justify-content:center;font-size:13px;font-weight:600;background:var(--red);color:#fff}
.band.mid .cta{background:#fff;color:var(--red)}
/* categories */
.cat-card{position:absolute;top:2535px;width:280px;height:345px;border:1px solid var(--line);border-radius:14px;overflow:hidden;background:#fff}
.cat-card .ph{height:190px}
.cat-card h5{font-size:17px;font-weight:600;line-height:21px;padding:20px 20px 0}
.cat-card p{font-size:12.5px;line-height:18px;color:var(--text);padding:14px 20px 0}
/* contact */
.info-row{display:flex;gap:10px;font-size:13px;line-height:18px;color:var(--text);margin-bottom:14px}
/* footer */
.site-footer{position:absolute;left:0;top:3580px;width:1200px;height:460px;background:var(--footer)}
.social{display:flex;gap:14px}
.social span{width:35px;height:35px;border-radius:50%;background:var(--red)}
.bottom-bar{position:absolute;left:0;top:4040px;width:1200px;height:70px;background:var(--black);color:#fff;font-size:13px;font-weight:600;display:flex;align-items:center;justify-content:center}
</style>
</head>
<body>

<header class="site-header">
  <div class="brand"><span class="brand-mark"></span>Wirenexa</div>
  <nav class="nav"><span class="active">Home</span><span>About Us</span><span>Services</span><span>Contact</span></nav>
  <div class="phone-btn">
    <svg width="15" height="15" viewBox="0 0 24 24" fill="none" stroke="#fff" stroke-width="2"><path d="M22 16.9v3a2 2 0 0 1-2.2 2 19.8 19.8 0 0 1-8.6-3.1 19.5 19.5 0 0 1-6-6A19.8 19.8 0 0 1 2.1 4.2 2 2 0 0 1 4.1 2h3a2 2 0 0 1 2 1.7c.1.9.4 1.8.7 2.7a2 2 0 0 1-.5 2.1L8 9.8a16 16 0 0 0 6 6l1.3-1.3a2 2 0 0 1 2.1-.4c.9.3 1.8.6 2.7.7a2 2 0 0 1 1.7 2z"/></svg>
    (888)-555-0142
  </div>
</header>

<section class="hero" role="img" aria-label="Server rack with bundles of blue network patch cables">
  <h1 class="hero-title">Professional<br>Cabling for IT &amp;<br>Security Systems</h1>
  <div class="hero-regions">VIRGINIA | WASHINGTON DC | MARYLAND</div>
  <form class="callback">
    <h2>Request Callback</h2>
    <div class="field">Name</div>
    <div class="field">Email</div>
    <div class="field">Phone</div>
    <div class="field msg">Message</div>
    <div class="captcha"><span class="box"></span>I'm not a robot</div>
    <div class="btn-red" style="margin-top:14px">Request Call</div>
  </form>
</section>

<section>
  <h2 class="h-sec center abs" style="left:0;top:890px;width:1200px">Elevate Your Connectivity with<br>Wirenexa's Cabling Solutions</h2>
  <p class="p-sec center abs" style="left:310px;top:992px;width:580px">Wirenexa is your premier provider of professional low voltage cabling for offices and industrial sites in Virginia, Washington DC, and Maryland. We deliver structured cabling for Wi-Fi, audio/video conference rooms, access control systems, CCTV, and more.</p>

  <div class="feature-photo" role="img" aria-label="Technician testing fiber cables in front of a patch panel"></div>
  <div class="features">
    <h3>Key Features of Our Cabling Services:</h3>
    <p><b>Experience:</b> Years of hands-on expertise delivering reliable cabling solutions for offices, businesses, and industrial facilities of all sizes.</p>
    <p><b>Comprehensive Solutions:</b> Complete low-voltage cabling services, including CAT6/CAT7, fiber optics, and Wi-Fi installations, customized for reliable performance and seamless connectivity.</p>
    <p><b>Quality Workmanship:</b> Precision-engineered cabling solutions delivered with attention to detail for reliable, durable, and long-lasting performance.</p>
    <p><b>Commercial and Industrial:</b> Expert cabling solutions for businesses, offices, warehouses, and data centers of all sizes.</p>
    <p><b>Customer Satisfaction:</b> We prioritize your needs, delivering tailored cabling solutions and exceptional service every step of the way.</p>
    <ul class="ticks">
      <li><svg width="16" height="16" viewBox="0 0 24 24" fill="none" stroke="#d42e22" stroke-width="2"><rect x="3" y="3" width="18" height="18" rx="3"/><path d="M8 12l3 3 8-8"/></svg>Copper CAT6 and CAT7</li>
      <li><svg width="16" height="16" viewBox="0 0 24 24" fill="none" stroke="#d42e22" stroke-width="2"><rect x="3" y="3" width="18" height="18" rx="3"/><path d="M8 12l3 3 8-8"/></svg>Single and Multimode Fiber</li>
      <li><svg width="16" height="16" viewBox="0 0 24 24" fill="none" stroke="#d42e22" stroke-width="2"><rect x="3" y="3" width="18" height="18" rx="3"/><path d="M8 12l3 3 8-8"/></svg>Wi-Fi Installation</li>
    </ul>
  </div>
</section>

<section>
  <h2 class="h-sec center abs" style="left:0;top:1648px;width:1200px">Why Choose Us</h2>
  <p class="p-sec center abs" style="left:330px;top:1704px;width:540px">We are a full service cabling company and will work with your IT staff to make sure everything up and running after installation and testing.</p>

  <div class="why-card hot" style="left:167px">
    <svg width="44" height="44" viewBox="0 0 24 24" fill="none" stroke="#fff" stroke-width="2"><path d="M12 2l8 3v6c0 5-3.5 9-8 11-4.5-2-8-6-8-11V5z"/><path d="M12 2v20"/></svg>
    <h4>Safe and Secure</h4>
    <p>Safe and secure cabling services for reliable, organized, and dependable network connectivity.</p>
    <span class="more">Learn More</span>
  </div>
  <div class="why-card" style="left:460px">
    <svg width="44" height="44" viewBox="0 0 24 24" fill="none" stroke="#111" stroke-width="2"><path d="M3 18v-6a9 9 0 0 1 18 0v6"/><rect x="3" y="14" width="4" height="7" rx="1"/><rect x="17" y="14" width="4" height="7" rx="1"/></svg>
    <h4>24/7 Support</h4>
    <p>Our 24/7 support team is always available to assist you whenever you need help.</p>
    <span class="more">Learn More</span>
  </div>
  <div class="why-card" style="left:753px">
    <svg width="44" height="44" viewBox="0 0 24 24" fill="none" stroke="#111" stroke-width="2"><rect x="3" y="5" width="18" height="15" rx="2"/><path d="M3 9h12"/><rect x="14" y="11" width="7" height="5" rx="1"/></svg>
    <h4>Low Cost</h4>
    <p>Our low-cost solutions provide reliable services without compromising on quality.</p>
    <span class="more">Learn More</span>
  </div>
</section>

<section>
  <div class="band" style="left:0;width:400px;background:var(--black)">
    <h4>Security Services</h4>
    <p>Access control and CCTV cabling to keep your building safe.</p>
    <span class="cta">Contact Us</span>
  </div>
  <div class="band mid" style="left:400px;width:400px;background:var(--red)">
    <h4>Commercial Services</h4>
    <p>Office low voltage cabling, Wi-Fi and AV for conference rooms.</p>
    <span class="cta">Contact Us</span>
  </div>
  <div class="band" style="left:800px;width:400px;background:var(--black)">
    <h4>Industrial Services</h4>
    <p>Structured cabling, IDF and MDF for warehouses, manufacturing facilities and others.</p>
    <span class="cta">Contact Us</span>
  </div>
</section>

<section>
  <h2 class="abs" style="left:167px;top:2618px;font-size:34px;font-weight:600;line-height:41px">Cable Installation<br>Categories</h2>
  <p class="p-sec abs" style="left:167px;top:2722px;width:265px">We provide network, data, voice, fiber optic, and structured cabling solutions, ensuring reliable performance and long-term connectivity.</p>

  <div class="cat-card" style="left:533px">
    <div class="ph" role="img" aria-label="Hands connecting blue patch cables into a switch" style="background:linear-gradient(135deg,#1a2b4a,#2f63c9 60%,#1b2a40)"></div>
    <h5>Voice &amp; Data Cable<br>Installations</h5>
    <p>We provide professional voice and data cabling for reliable connectivity and clear communication.</p>
  </div>
  <div class="cat-card" style="left:827px">
    <div class="ph" role="img" aria-label="Close-up of stripped copper network cables" style="background:linear-gradient(135deg,#5a8fb4,#2e8fd8 50%,#9aa3ab)"></div>
    <h5>Copper Cable CAT6 and<br>CAT7</h5>
    <p>We provide CAT6 and CAT7 cabling for fast, reliable, and secure connectivity.</p>
  </div>
  <div class="cat-card" style="left:1121px">
    <div class="ph" role="img" aria-label="Blue fiber optic cable connectors" style="background:linear-gradient(135deg,#1f6fc4,#5aa7e6)"></div>
    <h5>Fiber Cable Single &amp;<br>Multi Mode</h5>
    <p>We provide single and multi mode fiber for fast, secure &amp; high-performance links.</p>
  </div>
</section>

<section>
  <h2 class="h-sec center abs" style="left:0;top:2963px;width:1200px">Get in Touch</h2>
  <h3 class="abs" style="left:167px;top:3153px;font-size:20px;font-weight:600">Contact Us</h3>
  <div class="abs" style="left:167px;top:3196px;width:280px">
    <p class="p-sec" style="margin-bottom:16px">We provide complete cabling solutions and work with your IT team to ensure everything is running smoothly after installation and testing. Contact us today.</p>
    <div class="info-row"><svg width="16" height="16" viewBox="0 0 24 24" fill="none" stroke="#d42e22" stroke-width="2"><path d="M22 16.9v3a2 2 0 0 1-2.2 2 19.8 19.8 0 0 1-8.6-3.1 19.5 19.5 0 0 1-6-6A19.8 19.8 0 0 1 2.1 4.2 2 2 0 0 1 4.1 2h3a2 2 0 0 1 2 1.7c.1.9.4 1.8.7 2.7a2 2 0 0 1-.5 2.1L8 9.8a16 16 0 0 0 6 6l1.3-1.3a2 2 0 0 1 2.1-.4c.9.3 1.8.6 2.7.7a2 2 0 0 1 1.7 2z"/></svg><span>703-555-0198<br>(888) 555 -0142</span></div>
    <div class="info-row"><svg width="16" height="16" viewBox="0 0 24 24" fill="none" stroke="#d42e22" stroke-width="2"><rect x="3" y="5" width="18" height="14" rx="2"/><path d="M3 7l9 6 9-6"/></svg><span>sales@wirenexa.com</span></div>
    <div class="info-row"><svg width="16" height="16" viewBox="0 0 24 24" fill="none" stroke="#d42e22" stroke-width="2"><path d="M12 22s7-6.5 7-12a7 7 0 0 0-14 0c0 5.5 7 12 7 12z"/><circle cx="12" cy="10" r="2.5"/></svg><span>4100 Maple Ridge Dr, Suite 310<br>Vienna, VA 22182</span></div>
  </div>
  <form class="abs" style="left:533px;top:3063px;width:501px">
    <div class="field">Name</div>
    <div class="field">Email</div>
    <div class="field">Phone</div>
    <div class="field msg">Message</div>
    <div class="captcha" style="width:303px;margin-top:28px"><span class="box"></span>I'm not a robot</div>
    <div class="btn-red" style="margin-top:26px">Request Call</div>
  </form>
</section>

<footer class="site-footer">
  <div class="brand" style="top:117px;font-size:36px"><span class="brand-mark" style="width:26px;height:26px"></span>Wirenexa</div>
  <p class="p-sec abs" style="left:167px;top:190px;width:280px">Wirenexa is a local group of IT professionals, dedicated to fast, reliable and honest service. No job is too big or too small, get in touch today for solutions to all your IT infrastructure needs!</p>
  <div class="social abs" style="left:167px;top:307px"><span></span><span></span><span></span><span></span><span></span></div>
  <h4 class="abs" style="left:533px;top:112px;font-size:15px;font-weight:600">Useful Links</h4>
  <div class="abs" style="left:533px;top:150px;font-size:13px;line-height:31.5px;color:var(--text)">Home<br>About Us<br>Services<br>Contact</div>
  <div class="abs" role="img" aria-label="30 years anniversary badge" style="left:780px;top:135px;width:230px;height:130px;border-radius:12px;background:linear-gradient(135deg,#2aa84a,#2563c9 50%,#d43a7a)"></div>
</footer>

<div class="bottom-bar">Copyright © 2026 Wirenexa</div>

</body>
</html>
```